Business Card Design Project

I need some business cards with the logo you did for us (attached)
I am looking for a coulourful yet serious business card

We do market research
on the back I want the logo

on the front my name : Corinne Valdessac
position : Manager
address : Brume Analytica Sarl - 27 Rue des tanneurs
1847 Glarency - Switzerland
corinne.valdessac@brumeanalytica.ch
Tel : +4122 934 07 58
Mob France :+33 671 42 8356
Mob Italy +39 347 520 8163

The tree of the logo could also be used alone

THE BACKGROUND COLOR ON THE FRONT HAS TO BE WHITE, ON THE BACK YU CAN TRY OHER COLOUR BUT HOMOGENEOUS (NOT EXPENSIVE TO PRINT)

Target Market(s)

multinational companies or other market research companies

Industry/Entity Type

Market Research

Requirements
Must have
• logo on the back
and all the info above

```html
<!DOCTYPE html>
<html lang="en">
<head>
<meta charset="utf-8">
<title>Brume Analytica – Business Card</title>
<link rel="stylesheet" href="https://fonts.googleapis.com/css2?family=Barlow:wght@300;400;500;600&display=swap">
<style>
  :root {
    --backdrop: #d9d9d9;
    --card-white: #ffffff;
    --brand-pink: #e8058c;
    --brand-crimson: #c8224f;
    --info-dark: #9b1456;
    --swirl-grey: #ebe6e6;
    --swirl-white: #ffffff;
    --text-white: #ffffff;
  }
  * { margin: 0; padding: 0; box-sizing: border-box; }
  html, body {
    width: 900px;
    height: 1200px;
    overflow: hidden;
    background: var(--backdrop);
    font-family: "Barlow", sans-serif;
  }
  .canvas {
    position: relative;
    width: 900px;
    height: 1200px;
  }
  .card {
    position: absolute;
    left: 67px;
    width: 766px;
    height: 438px;
    border-radius: 22px;
    overflow: hidden;
  }
  .card--logo-side {
    top: 132px;
    background: var(--card-white);
  }
  .card--info-side {
    top: 639px;
    background: var(--brand-pink);
  }
  .swirl-field {
    position: absolute;
    top: 0;
    right: 0;
    width: 320px;
    height: 100%;
  }
  .swirl-field--grey {
    background: radial-gradient(ellipse at 65% 55%, var(--swirl-grey) 0%, rgba(235,230,230,0.7) 45%, rgba(235,230,230,0) 75%);
  }
  .swirl-field--white {
    background: radial-gradient(ellipse at 65% 55%, rgba(255,255,255,0.75) 0%, rgba(255,255,255,0.45) 45%, rgba(255,255,255,0) 75%);
  }
  .wordmark {
    position: absolute;
    left: 45px;
    top: 318px;
    font-size: 66px;
    font-weight: 500;
    line-height: 1;
    letter-spacing: -0.5px;
    color: var(--brand-crimson);
  }
  .contact {
    position: absolute;
    left: 48px;
    top: 164px;
    color: var(--info-dark);
  }
  .contact__name {
    font-size: 29px;
    font-weight: 300;
    line-height: 34px;
    color: var(--text-white);
  }
  .contact__role {
    font-size: 21px;
    font-weight: 500;
    line-height: 30px;
    letter-spacing: 0.5px;
  }
  .contact__line {
    font-size: 17.5px;
    font-weight: 500;
    line-height: 28.3px;
  }
  .contact__line--email {
    color: var(--text-white);
  }
</style>
</head>
<body>
<main class="canvas">
  <section class="card card--logo-side">
    <div class="swirl-field swirl-field--grey" role="img" aria-label="Faint grey swirl pattern decoration"></div>
    <div class="wordmark">brume analytica</div>
  </section>

  <section class="card card--info-side">
    <div class="swirl-field swirl-field--white" role="img" aria-label="White swirl pattern decoration"></div>
    <div class="contact">
      <p class="contact__name">Corinne Valdessac</p>
      <p class="contact__role">Manager</p>
      <p class="contact__line">Brume Analytica Sarl - 27 Rue des tanneurs</p>
      <p class="contact__line">1847 Glarency - Switzerland</p>
      <p class="contact__line contact__line--email">corinne.valdessac@brumeanalytica.ch</p>
      <p class="contact__line">tel:&nbsp; +4122 934 07 58</p>
      <p class="contact__line">mob france:&nbsp; +33 671 42 8356</p>
      <p class="contact__line">mob italy:&nbsp; +39 347 520 8163</p>
    </div>
  </section>
</main>
</body>
</html>
```